Pharmacist turned chef in Key West Fl needs a logo design

I am looking for a professional looking business card that says who I am and what I do. For example Chef Dale Morvik, natural organic and health supportive cooking. Phone 555-416-8870 email dalemorvik@quillpost.example web www.thesaltedharvest.example, Key West fl. The color or colors should have some green and other colors that look good together that stimulate appetite and give a clean healthy image. To help with a thought process, words like food as medicine, medicine is food, good nutrition is health but at the same time I do not want a lot of medical symbols that me it look clinical. Any questions please contact me.

```html
<!DOCTYPE html>
<html lang="en">
<head>
<meta charset="utf-8">
<title>Chef Dale Morvik — Business Card</title>
<link href="https://fonts.googleapis.com/css2?family=Questrial&display=swap" rel="stylesheet">
<style>
  :root {
    --page: #ffffff;
    --spine-dark: #0a0a0a;
    --spine-light: #5a5a5a;
    --green-deep: #4ea53a;
    --green-light: #98c93c;
    --orange: #f07f22;
    --yellow: #ffd800;
    --red: #ec1f26;
    --red-orange: #ef6a2a;
    --ink: #f4f4f4;
    --capsule-top: #19b4e6;
    --capsule-bottom: #0a86a8;
  }
  * { margin: 0; padding: 0; box-sizing: border-box; }
  html, body {
    width: 1200px; height: 1000px; overflow: hidden;
    background: var(--page);
  }
  .card {
    position: absolute; left: 58px; top: 223px;
    width: 1085px; height: 634px;
    font-family: "Questrial", "Century Gothic", sans-serif;
    color: var(--ink);
  }
  .card__spine {
    position: absolute; left: 0; top: 0; width: 52px; height: 100%;
    background: linear-gradient(180deg, var(--spine-dark) 0%, var(--spine-light) 45%, var(--spine-dark) 100%);
  }
  .band { position: absolute; left: 52px; right: 0; }
  .band--name {
    top: 0; height: 205px;
    background: radial-gradient(ellipse 45% 120% at 30% 10%, var(--green-light) 0%, var(--green-light) 20%, var(--green-deep) 100%);
  }
  .band--tagline {
    top: 205px; height: 97px;
    background: radial-gradient(ellipse 40% 140% at 45% 50%, var(--yellow) 0%, var(--orange) 100%);
    box-shadow: 0 -3px 6px rgba(0,0,0,.25), 0 3px 6px rgba(0,0,0,.3);
    z-index: 2;
  }
  .band--contact {
    top: 302px; bottom: 0;
    background: linear-gradient(100deg, var(--orange) 0%, var(--red-orange) 30%, var(--red) 55%, var(--red) 100%);
  }
  .text { position: absolute; white-space: nowrap; text-shadow: 1px 2px 3px rgba(0,0,0,.35); line-height: 1; }
  .title { left: 62px; top: 52px; font-size: 82px; }
  .name { left: 62px; top: 140px; font-size: 62px; }
  .tagline { left: 64px; top: 240px; font-size: 33px; z-index: 3; }
  .contact {
    position: absolute; right: 67px; top: 388px;
    text-align: right; font-size: 37px; line-height: 63px;
    text-shadow: 1px 2px 3px rgba(0,0,0,.35);
  }
  .emblem { position: absolute; left: 176px; top: 318px; }
</style>
</head>
<body>
  <main class="card">
    <div class="card__spine"></div>
    <div class="band band--name"></div>
    <div class="band band--tagline"></div>
    <div class="band band--contact"></div>

    <div class="text title">Chef</div>
    <div class="text name">Dale Morvik</div>
    <div class="text tagline">Natural organic and health supportive cooking</div>

    <svg class="emblem" width="122" height="254" viewBox="0 0 122 254" role="img" aria-label="Blue capsule emblem with knife and fork">
      <defs>
        <linearGradient id="capsuleFill" x1="0" y1="0" x2="0" y2="1">
          <stop offset="0" stop-color="var(--capsule-top)"/>
          <stop offset="1" stop-color="var(--capsule-bottom)"/>
        </linearGradient>
      </defs>
      <rect x="2" y="2" width="118" height="250" rx="59" fill="url(#capsuleFill)" stroke="#e8f4f8" stroke-width="4"/>
    </svg>

    <div class="contact">
      <div>phone 555-416-8870</div>
      <div>email dalemorvik@quillpost.example</div>
      <div>www.thesaltedharvest.example</div>
    </div>
  </main>
</body>
</html>
```